Webdesign/Updates

We would like a landing page for an online course for our educators. So a website with about 3 to 5 pages - Home, About US, Online course, blog, and Contact us. We have a wordpress site up using a template, but we are looking for something that connects more with our new logo.

Target Market(s)

Educators, workshop trainers/instructors, colleges, community schools, educational institutions, global organizations

Industry/Entity Type

Education

Contact Information for Business Card

Use the words below as place holders for the front:
Name
Title
Address line 1
Address line 2
Email
Phone
Website URL

--the back
Logo
1 short question, use "What do you 1234 about your program?"

Number of Pages Required

4 page

Requirements
Must have
• Home page
• Course Page
• Blog
• right side bar with social media content and invitation to subscribe to newsletter
• see logo colors in document
Nice to have
• Newsletter Page with graphic that can be on this page or page can be sent as a pdf via email or in an email.
Should not have
• Be better than attached description
• clean simple look but stylish

```html
<!DOCTYPE html>
<html lang="en">
<head>
<meta charset="utf-8">
<title>Ready Set Teach – Online Course Design Program</title>
<link href="https://fonts.googleapis.com/css2?family=Montserrat:wght@400;500;600;700&display=swap" rel="stylesheet">
<style>
:root{
  --green:#a6ce39;
  --blue:#1fa3dc;
  --blue-dark:#1679b8;
  --orange:#ef6c1a;
  --navy:#0c2b3e;
  --ink:#2c2c2c;
  --muted:#8a8a8a;
  --pale-blue:#e8f3fa;
  --white:#ffffff;
}
*{margin:0;padding:0;box-sizing:border-box}
html,body{width:1200px;height:3888px;overflow:hidden}
body{font-family:'Montserrat',sans-serif;color:var(--ink);background:var(--white);position:relative}
.abs{position:absolute}
.backdrop{position:absolute;left:0;top:0;width:1200px;height:3888px}

/* header */
.logo{left:174px;top:88px;font-size:34px;font-weight:700;letter-spacing:6px;color:var(--ink)}
.nav{left:609px;top:81px;display:flex;gap:20px;font-size:10.5px;font-weight:700;color:var(--white);text-transform:uppercase;white-space:nowrap}
.btn{display:flex;align-items:center;justify-content:center;border-radius:40px;font-size:12px;font-weight:500}
.btn-green{background:var(--green);color:var(--white)}
.btn-white{background:var(--white);color:var(--orange)}
.login{left:987px;top:70px;width:125px;height:34px}

/* hero */
.hero-tagline{right:72px;top:205px;width:400px;text-align:right;color:var(--white)}
.hero-tagline h2{font-size:27px;font-weight:500;margin-bottom:14px}
.hero-tagline p{font-size:13px;line-height:17px}
.register{left:174px;top:200px;width:300px}
.register h1{font-size:27px;font-weight:500;color:var(--blue)}
.register .trust{font-size:13px;color:var(--muted);margin-top:10px}
.register .trust b{color:var(--orange)}
.register .intro{font-size:12px;color:var(--muted);line-height:17px;margin-top:20px}
.field{left:174px;width:259px;height:26px;border-bottom:1px solid #cfcfcf;font-size:11px;color:#a0a0a0;padding-top:4px;padding-left:6px}
.register-btn{left:174px;top:446px;width:181px;height:36px}

/* features */
.features-head{left:174px;top:743px}
.features-head h2{font-size:22px;font-weight:500;color:var(--blue);line-height:28px}
.features-head p{font-size:12px;color:var(--muted);margin-top:10px}
.feature{width:412px;height:89px;background:var(--white);box-shadow:0 4px 14px rgba(0,0,0,.12);display:flex;align-items:center;padding-left:40px;gap:30px}
.feature h3{font-size:12px;font-weight:700;color:var(--orange)}
.feature p{font-size:12px;color:var(--orange);line-height:15px;margin-top:2px}
.feature.is-active{background:var(--green)}
.feature.is-active h3,.feature.is-active p{color:var(--white)}
.feature svg{flex:none}

.program-head{left:400px;top:1172px;width:410px;text-align:center;color:var(--white)}
.program-head h2{font-size:21px;font-weight:700;line-height:27px}
.program-head p{font-size:12px;line-height:16px;margin-top:18px}

/* course */
.course{left:174px;top:1465px;width:360px;color:var(--white)}
.course h3{font-size:15px;font-weight:700}
.course h3 span{font-weight:500;color:#ffd9bf;margin-left:8px}
.course p{font-size:12px;line-height:15px;margin-top:14px}
.course-btn{left:174px;top:1594px;width:129px;height:34px}
.video{left:601px;top:1381px;width:441px;height:299px;background:linear-gradient(135deg,#d9d2c6,#8f7e6c 60%,#3b3a44);box-shadow:0 10px 24px rgba(0,0,0,.3)}
.play{left:796px;top:1503px}

.attention{left:174px;top:1810px;width:520px;color:var(--white)}
.attention h2{font-size:21px;font-weight:500}
.attention p{font-size:12px;line-height:15px;margin-top:12px}
.attention-btn{left:174px;top:1931px;width:186px;height:36px}
.phone{left:920px;top:1720px;width:280px;height:400px;background:linear-gradient(160deg,#3a3a44,#d8406e 55%,#5a7fd8)}

/* instructors */
.instructor{top:2131px;width:261px;height:279px;background:var(--white);box-shadow:0 4px 14px rgba(0,0,0,.13)}
.instructor .photo{height:168px}
.instructor h4{font-size:15px;font-weight:500;margin:22px 0 0 24px}
.instructor p{font-size:12px;color:var(--muted);line-height:15px;margin:6px 24px 0}
.dots{display:flex;gap:9px}
.dots i{width:7px;height:7px;border-radius:50%;background:#c6d9e6;display:block}
.dots i.on{background:var(--blue)}
.instructors-text{left:728px;top:2198px;width:330px}
.instructors-text h2{font-size:21px;font-weight:500;color:var(--blue);line-height:25px}
.instructors-text p{font-size:12px;color:var(--muted);line-height:15px;margin-top:14px}
.more-btn{left:728px;top:2325px;width:148px;height:34px}

/* objectives */
.objectives-head{left:0;top:2548px;width:1200px;text-align:center}
.objectives-head h2{font-size:20px;font-weight:500;color:var(--blue)}
.objectives-head p{font-size:12px;color:var(--muted);margin-top:10px}
.objective{top:2680px;width:220px;text-align:center}
.objective h3{font-size:15px;font-weight:500;color:var(--blue);margin-top:14px}
.objective p{font-size:12px;color:var(--muted);line-height:15px;margin-top:8px}
.coffee{left:925px;top:2850px;width:275px;height:285px;background:linear-gradient(135deg,#e6e6e6,#3a2a24 60%,#1a1110)}

/* testimonial */
.testimonial{left:174px;top:3025px;width:852px;height:505px;background:var(--white);box-shadow:0 6px 20px rgba(0,0,0,.12);text-align:center}
.quote-mark{position:absolute;left:0;top:20px;width:100%;font-size:190px;line-height:190px;color:#ececec;font-weight:700}
.testimonial h2{position:absolute;top:170px;width:100%;font-size:20px;font-weight:500;color:var(--blue)}
.avatar{position:absolute;left:373px;top:208px;width:106px;height:106px;border-radius:50%;background:linear-gradient(135deg,#c79a7a,#5b3a2a)}
.testimonial p{position:absolute;left:145px;top:337px;width:562px;font-size:12px;color:var(--muted);line-height:15px}
.testimonial .dots{position:absolute;left:402px;top:400px}

/* footer */
.footer-logo{left:249px;top:3588px;font-size:26px;letter-spacing:7px;color:var(--white)}
.footer-about{left:249px;top:3629px;width:230px;font-size:11px;color:var(--white);line-height:13px}
.footer-col{top:3590px;font-size:11px;color:var(--white);line-height:14px}
.footer-col h4{font-size:12px;font-weight:700;margin-bottom:8px}
.btn-outline{border:2px solid var(--white);color:var(--white)}
.btn-solid{background:var(--white);color:var(--blue)}
.footer-bar{left:0;top:3810px;width:1200px;height:78px;background:var(--navy)}
.copyright{left:249px;top:3843px;font-size:11px;color:#6f8a9c}
.social{left:790px;top:3840px;display:flex;gap:24px}
.social i{display:block;width:14px;height:14px;border-radius:50%;background:var(--white)}
</style>
</head>
<body>

<svg class="backdrop" viewBox="0 0 1200 3888" aria-hidden="true">
  <defs>
    <linearGradient id="classroom" x1="0" y1="0" x2="1" y2="1">
      <stop offset="0" stop-color="#3a3d3a"/><stop offset=".6" stop-color="#6b5a44"/><stop offset="1" stop-color="#2d3b3f"/>
    </linearGradient>
    <linearGradient id="desk" x1="0" y1="0" x2="1" y2="1">
      <stop offset="0" stop-color="#3d3833"/><stop offset=".5" stop-color="#7b6f64"/><stop offset="1" stop-color="#a49a90"/>
    </linearGradient>
  </defs>
  <circle cx="1040" cy="110" r="510" fill="var(--blue)"/>
  <circle cx="990" cy="40" r="530" fill="var(--green)"/>
  <circle cx="1015" cy="60" r="500" fill="url(#classroom)" role="img" aria-label="Lecture hall full of students working on laptops"/>
  <rect x="0" y="640" width="1200" height="820" fill="url(#desk)" role="img" aria-label="Student writing notes at a desk"/>
  <path d="M0 600 H1200 V670 C1000 640 760 700 620 860 C480 1020 300 1120 0 1090 Z" fill="var(--white)"/>
  <path d="M0 1330 C260 1250 520 1420 820 1330 C980 1285 1100 1260 1200 1250 V2100 H0 Z" fill="var(--orange)"/>
  <path d="M0 2085 C380 2100 650 1980 880 1890 C1020 1835 1130 1830 1200 1840 V2130 H0 Z" fill="var(--white)"/>
  <circle cx="0" cy="2650" r="190" fill="var(--pale-blue)"/>
  <path d="M0 2790 C90 2960 280 3060 580 3060 C880 3060 1080 3030 1200 2990 V3810 H0 Z" fill="var(--blue)"/>
</svg>

<!-- header -->
<div class="abs logo">LOGO</div>
<nav class="abs nav"><span>Home</span><span>Course</span><span>Blog</span><span>Consulting</span><span>About Me</span></nav>
<div class="abs btn btn-green login">Portal Log In</div>

<!-- hero -->
<div class="abs hero-tagline">
  <h2>Ready Set Teach</h2>
  <p>Get Comfortable, confident and satisfied teaching online with the Ultimate Course Design Program. A comprehensive Program For Building accredited online courses</p>
</div>
<div class="abs register">
  <h1>Register Now!</h1>
  <p class="trust">Trusted by <b>500+</b> Students</p>
  <p class="intro">Join our community of student around the world helping you succeed</p>
</div>
<div class="abs field" style="top:340px">Enter your name</div>
<div class="abs field" style="top:389px">Enter your email address</div>
<div class="abs btn btn-green register-btn">Get it now</div>

<!-- features -->
<div class="abs features-head">
  <h2>The Ultimate Course<br>Design Program Features</h2>
  <p>A Collaborative Approach to Creating Accredited Online Course</p>
</div>
<div class="abs feature is-active" style="left:174px;top:850px">
  <svg width="36" height="44" viewBox="0 0 36 44" fill="none" stroke="#fff" stroke-width="2"><rect x="4" y="2" width="28" height="40" rx="3"/><line x1="11" y1="12" x2="25" y2="12"/><line x1="11" y1="20" x2="25" y2="20"/><line x1="11" y1="28" x2="20" y2="28"/></svg>
  <div><h3>Effective Lessons</h3><p>Lorem ipsum dolor sit amet,<br>consectetur adipiscing elit, sed do</p></div>
</div>
<div class="abs feature" style="left:614px;top:850px">
  <svg width="44" height="44" viewBox="0 0 44 44" fill="none" stroke="var(--green)" stroke-width="2"><rect x="6" y="10" width="32" height="26" rx="2"/><path d="M14 24l5 5 11-11"/><line x1="6" y1="40" x2="38" y2="40"/></svg>
  <div><h3>Awesome Quizes</h3><p>Lorem ipsum dolor sit amet,<br>consectetur adipiscing elit, sed do</p></div>
</div>
<div class="abs feature" style="left:174px;top:956px">
  <svg width="44" height="44" viewBox="0 0 44 44" fill="none" stroke="var(--green)" stroke-width="2"><rect x="4" y="6" width="36" height="30" rx="2"/><path d="M18 14l10 7-10 7z"/><line x1="10" y1="40" x2="34" y2="40"/></svg>
  <div><h3>Quality Videos</h3><p>Lorem ipsum dolor sit amet,<br>consectetur adipiscing elit, sed do</p></div>
</div>
<div class="abs feature" style="left:614px;top:956px">
  <svg width="44" height="44" viewBox="0 0 44 44" fill="none" stroke="var(--green)" stroke-width="2"><path d="M4 24v14h36V24"/><path d="M22 4v22M14 18l8 8 8-8"/></svg>
  <div><h3>Hosted Content</h3><p>Lorem ipsum dolor sit amet,<br>consectetur adipiscing elit, sed do</p></div>
</div>

<div class="abs program-head">
  <h2>The Ultimate Course<br>Design Program</h2>
  <p>A practical Comprehensive Approach<br>that gets you ahead</p>
</div>

<!-- course -->
<div class="abs course">
  <h3>Cousre title <span>48mins</span></h3>
  <p>Lorem ipsum dolor sit amet, consectetur adipiscing elit, sed do eiusmod tempor incididunt ut labore et dolore magna aliqua. Ut enim ad minim veniam.Lorem ipsum dolor sit amet, consectetur adipiscing elit, sed do</p>
</div>
<div class="abs btn btn-green course-btn">Learn More</div>
<div class="abs video" role="img" aria-label="Course video preview of students taking notes"></div>
<svg class="abs play" width="52" height="52" viewBox="0 0 52 52" aria-hidden="true"><circle cx="26" cy="26" r="26" fill="var(--white)"/><path d="M21 15l16 11-16 11z" fill="var(--green)"/></svg>

<div class="abs attention">
  <h2>Got your attention now?</h2>
  <p>The Ultimate Course Design Promgram will teach you Lorem ipsum dolor sit amet, consectetur adipiscing elit, sed do eiusmod tempor incididunt ut labore et dolore magna aliqua. Ut enim ad minim veniam.Lorem ipsum dolor sit amet, consectetur adipiscing elit, sed do</p>
</div>
<div class="abs btn btn-white attention-btn">Get Started</div>
<div class="abs phone" role="img" aria-label="Photo of a smartphone with a colourful screen"></div>

<!-- instructors -->
<div class="abs instructor" style="left:-157px">
  <div class="photo" role="img" aria-label="Instructor portrait" style="background:linear-gradient(135deg,#dfe3e6,#6b7580)"></div>
  <h4>Tempor B. elit</h4><p>consectetur adipiscing elit, sed do</p>
</div>
<div class="abs instructor" style="left:124px">
  <div class="photo" role="img" aria-label="Instructor portrait in front of a chalkboard" style="background:linear-gradient(135deg,#3f8a78,#2a5c52)"></div>
  <h4>Adipiscing A. elit</h4><p>consectetur adipiscing elit,<br>sed do</p>
</div>
<div class="abs instructor" style="left:404px">
  <div class="photo" role="img" aria-label="Instructor portrait in front of a chalkboard" style="background:linear-gradient(135deg,#355e4d,#1f3a30)"></div>
  <h4>Magna C. aliqua</h4><p>consectetur adipiscing elit,<br>sed do</p>
</div>
<div class="abs dots" style="left:622px;top:2426px"><i></i><i class="on"></i><i class="on"></i></div>
<div class="abs instructors-text">
  <h2>Meet Our Experienced<br>&amp; Enthusiastic Instructors</h2>
  <p>Lorem ipsum dolor sit amet, consectetur adipiscing elit, sed do eiusmod tempor incididunt ut labore et dolore magna aliqua. Ut enim ad minim veniam.</p>
</div>
<div class="abs btn btn-green more-btn">More</div>

<!-- objectives -->
<div class="abs objectives-head">
  <h2>Learing Objectives</h2>
  <p>So many objective goals that we expect you achieve</p>
</div>
<div class="abs objective" style="left:266px">
  <svg width="62" height="62" viewBox="0 0 62 62" fill="none" stroke="var(--ink)" stroke-width="2.5"><path d="M10 52l26-26M30 14l10-6 8 8-6 10z"/><path d="M52 52L20 20M14 10a8 8 0 0 0 6 10"/></svg>
  <h3>Skills</h3><p>Lorem ipsum dolor sit amet, consectetur adipiscing elit, sed do eiusmod tempor incididunt ut labore et dolore magna aliqua. Ut</p>
</div>
<div class="abs objective" style="left:491px">
  <svg width="62" height="62" viewBox="0 0 62 62" fill="none" stroke="var(--ink)" stroke-width="2.5"><circle cx="31" cy="16" r="7"/><path d="M18 40c0-8 6-13 13-13s13 5 13 13"/><rect x="12" y="38" width="38" height="14" rx="2"/><line x1="6" y1="56" x2="56" y2="56"/></svg>
  <h3>Self Learning</h3><p>Lorem ipsum dolor sit amet, consectetur adipiscing elit, sed do eiusmod tempor incididunt ut labore et dolore magna aliqua. Ut</p>
</div>
<div class="abs objective" style="left:701px">
  <svg width="62" height="62" viewBox="0 0 62 62" fill="none" stroke="var(--ink)" stroke-width="2.5"><path d="M20 56V44c-6-4-10-10-10-18a21 21 0 0 1 42 0l4 10h-6v8h-9v12"/><circle cx="31" cy="26" r="6"/><path d="M31 14v4M31 34v4M19 26h4M39 26h4"/></svg>
  <h3>Knowledge</h3><p>Lorem ipsum dolor sit amet, consectetur adipiscing elit, sed do eiusmod tempor incididunt ut labore et dolore magna aliqua. Ut</p>
</div>

<!-- testimonial -->
<div class="abs testimonial">
  <div class="quote-mark">&rdquo;</div>
  <h2>What they say about us</h2>
  <div class="avatar" role="img" aria-label="Portrait of a student"></div>
  <p>Lorem ipsum dolor sit amet, consectetur adipiscing elit, sed do eiusmod tempor incididunt ut labore et dolore magna aliqua. Ut enim ad minim veniam, quis nostrud exercitation ullamco laboris nisi ut aliquip ex ea commodo consequat.</p>
  <div class="dots"><i></i><i class="on"></i><i class="on"></i></div>
</div>
<div class="abs coffee" role="img" aria-label="Photo of a cup of black coffee seen from above"></div>

<!-- footer -->
<div class="abs footer-logo">LOGO</div>
<p class="abs footer-about">Lorem ipsum dolor sit amet, consectetur adipiscing elit, sed do eiusmod tempor incididunt ut labore et dolore magna aliqua</p>
<div class="abs footer-col" style="left:508px"><h4>Content</h4>Get Started<br>Watch Videos<br>Contact us</div>
<div class="abs footer-col" style="left:651px"><h4>Quick Links</h4>Home<br>Courses<br>Consulting<br>About Me</div>
<div class="abs btn btn-outline" style="left:760px;top:3616px;width:150px;height:34px">Watch Videos</div>
<div class="abs btn btn-solid" style="left:760px;top:3668px;width:150px;height:34px">Get Started</div>

<div class="abs footer-bar"></div>
<div class="abs copyright">Copyright © Ready Set Teach. All Rights Reserved</div>
<div class="abs social" aria-label="Social links"><i></i><i></i><i></i><i></i><i></i></div>

</body>
</html>
```